Business Card Design Project

Business Card
We are rebranding with a new logo
Industry/Entity Type
Business
Contact Information for Business Card
Dennis Marlow +61 427581962 dennis@qovo.com.au P.O. Box 872 Kelvindale QLD 4309
Requirements
Must have
- Logo

```html
<!DOCTYPE html>
<html lang="en">
<head>
<meta charset="utf-8">
<title>Dennis Marlow – Business Card</title>
<link rel="stylesheet" href="https://fonts.googleapis.com/css2?family=Montserrat:wght@600;700&family=Open+Sans:wght@400&display=swap">
<style>
  :root {
    --card-w: 1200px;
    --card-h: 717px;
    --blue-deep: #5b6388;
    --blue-mid: #7fa9cc;
    --blue-light: #92d6f3;
    --blue-brand: #1b8ac4;
    --blue-stripe: #2a7fb0;
    --orange: #f08a2c;
    --orange-dark: #e2611b;
    --white: #ffffff;
    --grey-light: #ededee;
    --grey-soft: #f8f8f8;
  }
  * { margin: 0; padding: 0; box-sizing: border-box; }
  html, body {
    width: var(--card-w);
    height: var(--card-h);
    overflow: hidden;
    background: var(--white);
  }
  .card {
    position: relative;
    width: var(--card-w);
    height: var(--card-h);
    overflow: hidden;
    background:
      radial-gradient(ellipse 520px 420px at 560px 330px, rgba(160, 225, 250, 0.9), rgba(160, 225, 250, 0) 70%),
      linear-gradient(150deg, var(--blue-mid) 0%, var(--blue-light) 45%, #8dbad8 70%, var(--blue-deep) 100%);
  }
  .card__shapes {
    position: absolute;
    inset: 0;
    width: 100%;
    height: 100%;
  }
  .identity {
    position: absolute;
    left: 100px;
    top: 188px;
    width: 390px;
    text-align: center;
  }
  .identity__name {
    font-family: "Montserrat", sans-serif;
    font-weight: 700;
    font-size: 39px;
    letter-spacing: 1.5px;
    color: var(--white);
    line-height: 1.1;
  }
  .identity__title {
    font-family: "Montserrat", sans-serif;
    font-weight: 600;
    font-size: 27px;
    color: var(--orange);
    line-height: 1.2;
    margin-top: 2px;
    margin-right: 60px;
  }
  .contacts {
    position: absolute;
    left: 112px;
    top: 346px;
    list-style: none;
  }
  .contacts__item {
    display: flex;
    align-items: flex-start;
    gap: 38px;
    margin-bottom: 16px;
    font-family: "Open Sans", sans-serif;
    font-size: 25px;
    line-height: 34px;
    color: var(--white);
  }
  .contacts__icon {
    flex: none;
    width: 40px;
    height: 42px;
    border-radius: 3px;
    background: var(--orange);
    display: flex;
    align-items: center;
    justify-content: center;
  }
  .contacts__icon svg { width: 26px; height: 26px; }
  .brand {
    position: absolute;
    left: 710px;
    top: 300px;
    width: 330px;
    text-align: center;
    font-family: "Montserrat", sans-serif;
    font-weight: 700;
    color: var(--blue-brand);
  }
  .brand__name {
    font-size: 92px;
    line-height: 1;
  }
  .brand__sub {
    font-size: 28px;
    letter-spacing: 4px;
    margin-top: 16px;
  }
</style>
</head>
<body>
<div class="card">
  <svg class="card__shapes" viewBox="0 0 1200 717" aria-hidden="true">
    <defs>
      <linearGradient id="panel-white" x1="0" y1="0" x2="1" y2="1">
        <stop offset="0" stop-color="var(--grey-soft)"/>
        <stop offset="1" stop-color="var(--grey-light)"/>
      </linearGradient>
    </defs>
    <path class="stripe-orange" fill="var(--orange-dark)"
      d="M690 0 C560 40 505 170 545 285 C560 330 585 360 610 385 C570 340 548 290 552 230 C560 130 620 50 720 0 Z"/>
    <path class="stripe-orange-light" fill="var(--orange)"
      d="M705 0 C590 45 535 170 560 280 C570 320 590 350 610 385 C585 330 575 280 580 230 C590 130 640 55 730 0 Z"/>
    <path class="stripe-blue" fill="var(--blue-stripe)"
      d="M610 385 C680 450 715 530 700 620 C692 665 680 695 672 717 L690 717 C705 680 718 640 718 600 C718 510 680 440 610 385 Z"/>
    <path class="panel-white" fill="url(#panel-white)"
      d="M730 0 C640 55 590 130 580 230 C575 290 590 340 612 387 C680 450 718 520 716 600 C714 640 703 680 690 717 L1200 717 L1200 0 Z"/>
  </svg>

  <div class="identity">
    <h1 class="identity__name">DENNIS MARLOW</h1>
    <p class="identity__title">JOB TITLE</p>
  </div>

  <ul class="contacts">
    <li class="contacts__item">
      <span class="contacts__icon">
        <svg viewBox="0 0 24 24"><path fill="#fff" d="M6.6 10.8a15.1 15.1 0 0 0 6.6 6.6l2.2-2.2c.3-.3.7-.4 1-.2 1.1.4 2.3.6 3.6.6.6 0 1 .4 1 1V20c0 .6-.4 1-1 1A17 17 0 0 1 3 4c0-.6.4-1 1-1h3.5c.6 0 1 .4 1 1 0 1.3.2 2.5.6 3.6.1.3 0 .7-.2 1z"/></svg>
      </span>
      <span class="contacts__text">+61 427581962</span>
    </li>
    <li class="contacts__item">
      <span class="contacts__icon">
        <svg viewBox="0 0 24 24"><path fill="none" stroke="#fff" stroke-width="2" d="M3 6h18v12H3z M3 6l9 7 9-7"/></svg>
      </span>
      <span class="contacts__text">dennis@qovo.com.au</span>
    </li>
    <li class="contacts__item">
      <span class="contacts__icon">
        <svg viewBox="0 0 24 24"><path fill="#fff" d="M7 3h10a4 4 0 0 1 4 4v11h-7v3h-4v-3H3V7a4 4 0 0 1 4-4z"/><path fill="none" stroke="#f08a2c" stroke-width="1.6" d="M7 9h10v6H7z M7 9l5 3.5 5-3.5"/></svg>
      </span>
      <span class="contacts__text">P.O. Box 872 Kelvindale<br>QLD 4309</span>
    </li>
  </ul>

  <div class="brand">
    <p class="brand__name">Qovo</p>
    <p class="brand__sub">INTERNATIONAL</p>
  </div>
</div>
</body>
</html>
```